Corporate Design für Projektmanagement Firma
Vielen Dank für die Erarbeitung des Gewinnerdesigns. Auf Anfragen zur Anpassung von Designvorschlägen wurde prompt und mit ausgezeichneten Arbeitsergebnissen reagiert. Interessanterweise war gleich das erste Design das Gewinnerdesign - es wurde also auf Grundlage meiner Projektbeschreibung gleich das richtige Format getroffen. Hut ab! Danke auch für die unkomplizierte Übergabe der Dateien. Ich kann R olek auf jeden Fall weiterempfehlen.
Zielgruppe
Die Firma erbringt Projektmanagement- und Projektsteuerungsleistungen in der Baubranche für öffentliche Auftraggeber (größerer Anteil) und private Bauherren (kleinerer Anteil). Sie bietet außerdem strategische Organisationsberatung an, wenn es darum geht ein Projekt von Beginn an optimal aufzusetzen. Agiles Projektmanagement (in der Baubranche) ist ein Thema welches wir gern entwickeln wollen.
Aufgabenstellung
Die zu repräsentierende Firma lautet "Marlox Projektmanagement GmbH". Das Logo könnte die Initialen MaPM enthalten, gern mit kleinem e, oder auch nur kleine Buchstaben. Im Briefkopf und auf der Visitenkarte sollte der Firmenname ausgeschrieben auftauchen (ggf. in Kombi mit einem Logo?).
Eine mögliche Idee wäre die Verwendung eines Dreiecks als Symbol der Projektsteuerung- quasi das goldene Dreieck der Projektsteuerung (Kosten, Termine, Qualitäten). Das Design sollte eher schlicht, edel und geradlinig sein, nicht verspielt.

```html
<!DOCTYPE html>
<html lang="de">
<head>
<meta charset="utf-8">
<title>Marlox Projektmanagement GmbH – Geschäftsausstattung</title>
<link href="https://fonts.googleapis.com/css2?family=Roboto:wght@400;500;700&display=swap" rel="stylesheet">
<style>
  :root {
    --navy: #0b1f3f;
    --blue: #1a6fa8;
    --paper: #ffffff;
    --shadow: #e6e8ea;
    --edge: #c9cdd2;
    --bg: #ffffff;
  }
  * { margin: 0; padding: 0; box-sizing: border-box; }
  html, body {
    width: 1200px; height: 960px; overflow: hidden;
    background: var(--bg);
    font-family: "Roboto", Arial, sans-serif;
  }
  .stage { position: relative; width: 1200px; height: 960px; }

  .shadow { position: absolute; background: var(--shadow); }

  .sheet {
    position: absolute; background: var(--paper);
    border: 1px solid var(--edge);
  }

  /* Letterhead */
  .letterhead { left: 248px; top: 35px; width: 680px; height: 885px; }
  .letterhead-shadow { left: 260px; top: 60px; width: 684px; height: 877px; }

  .wordmark { text-align: center; color: var(--navy); }
  .wordmark .initials {
    display: flex; align-items: center; justify-content: center; gap: 6px;
    font-weight: 700; letter-spacing: 0.5px;
  }
  .wordmark .dot { display: inline-block; background: var(--blue); }
  .wordmark .name { font-weight: 400; line-height: 1.25; }

  .letterhead .wordmark { position: absolute; left: 52px; top: 22px; width: 140px; }
  .letterhead .initials { font-size: 30px; }
  .letterhead .dot { width: 12px; height: 12px; }
  .letterhead .name { font-size: 10.5px; margin-top: 6px; }

  .contact {
    position: absolute; text-align: right; color: var(--navy);
    font-weight: 700; line-height: 1.3;
  }
  .letterhead .contact { right: 30px; top: 33px; font-size: 11.5px; }

  .footer-address {
    position: absolute; left: 0; right: 0; top: 821px;
    text-align: center; color: var(--blue); font-weight: 700; font-size: 11.5px;
  }
  .rule-blue { position: absolute; left: 0; right: 0; background: var(--blue); }
  .band-navy { position: absolute; left: 0; right: 0; bottom: 0; background: var(--navy); }
  .letterhead .rule-blue { top: 845px; height: 4px; }
  .letterhead .band-navy { height: 28px; }

  /* Card front */
  .card-front-shadow { left: 210px; top: 259px; width: 403px; height: 229px; }
  .card-front {
    left: 202px; top: 251px; width: 403px; height: 229px;
    background: var(--navy); border: none;
  }
  .card-front .wordmark { position: absolute; left: 0; right: 0; top: 82px; color: var(--paper); }
  .card-front .initials { font-size: 44px; }
  .card-front .dot { width: 16px; height: 16px; }
  .card-front .name { font-size: 15px; margin-top: 10px; }

  /* Card back */
  .card-back-shadow { left: 591px; top: 519px; width: 405px; height: 230px; }
  .card-back { left: 581px; top: 509px; width: 405px; height: 230px; }
  .card-back .wordmark { position: absolute; left: 14px; top: 30px; width: 170px; }
  .card-back .initials { font-size: 30px; }
  .card-back .dot { width: 11px; height: 11px; }
  .card-back .name { font-size: 10px; margin-top: 5px; }
  .card-back .contact { right: 22px; top: 22px; font-size: 10.5px; }

  .person { position: absolute; left: 16px; top: 144px; font-weight: 700; }
  .person .person-name { color: var(--navy); font-size: 14px; }
  .person .person-role { color: var(--blue); font-size: 14px; margin-top: 3px; }

  .card-address {
    position: absolute; right: 22px; top: 141px; text-align: right;
    color: var(--blue); font-weight: 700; font-size: 10.5px; line-height: 1.3;
  }
  .card-back .rule-blue { top: 199px; height: 4px; }
  .card-back .band-navy { height: 19px; }
</style>
</head>
<body>
<main class="stage">

  <div class="shadow letterhead-shadow"></div>
  <section class="sheet letterhead" aria-label="Briefbogen">
    <div class="wordmark">
      <div class="initials"><span class="dot"></span>MaPM</div>
      <div class="name">Marlox Projektmanagement<br>GmbH</div>
    </div>
    <div class="contact">
      tel : 000.000.0000<br>
      Mob : 555.014.2290<br>
      Fax : 000.000.0000<br>
      jonka@marloxprojekt.com
    </div>
    <p class="footer-address">000 Sample Street Address, Suite 1111. Munchen, Germain 222222</p>
    <div class="rule-blue"></div>
    <div class="band-navy"></div>
  </section>

  <div class="shadow card-front-shadow"></div>
  <section class="sheet card-front" aria-label="Visitenkarte Vorderseite">
    <div class="wordmark">
      <div class="initials"><span class="dot"></span>MaPM</div>
      <div class="name">Marlox Projektmanagement<br>GmbH</div>
    </div>
  </section>

  <div class="shadow card-back-shadow"></div>
  <section class="sheet card-back" aria-label="Visitenkarte Rückseite">
    <div class="wordmark">
      <div class="initials"><span class="dot"></span>MaPM</div>
      <div class="name">Marlox Projektmanagement<br>GmbH</div>
    </div>
    <div class="contact">
      tel : 000.000.0000<br>
      Mob : 555.014.2290<br>
      Fax : 000.000.0000<br>
      jonka@marloxprojekt.com<br>
      www.marloxprojekt.com
    </div>
    <div class="person">
      <div class="person-name">jonka</div>
      <div class="person-role">staff engineering</div>
    </div>
    <div class="card-address">
      000 Sample Street Address<br>
      Suite 1111<br>
      Munchen, Germain 222222
    </div>
    <div class="rule-blue"></div>
    <div class="band-navy"></div>
  </section>

</main>
</body>
</html>
```